Harlow Ridge Growers and Nursery needs a business street sign.

I have three businesses located at the same address: The Harlow Ridge Growers & Nursery, The Bramble Nook, and The Quarry Commons. I am looking for a 4’ x 8’ street sign to represent all three businesses as one retail experience. It needs to be eye catching yet simple enough that people can fully read it while driving by. I have logos for the greenhouse and village however I do not have anything for The Bramble Nook. I’m looking for some type of font that’s similar or in between the two attached logos for The Bramble Nook.

• Horizontal Sign, Eye catching, yet simple design so people see it while driving by.
• Horizontal Sign
• I’m open to the design being both vertical and horizontal. Please provide both options

```html
<!DOCTYPE html>
<html lang="en">
<head>
<meta charset="UTF-8">
<title>The Harlow Ridge Experience – Street Sign</title>
<link href="https://fonts.googleapis.com/css2?family=Cinzel:wght@600;700;800&display=swap" rel="stylesheet">
<style>
  :root {
    --page-bg: #9fb1d6;
    --sign-white: #ffffff;
    --forest-green: #0f6433;
    --clay-tan: #c8937a;
    --rose-pink: #b8558a;
    --brick-maroon: #8e2b2b;
    --sage-glow: #dbe9b8;
    --meadow-green: #7e9a63;
    --blossom-pink: #e9b3a4;
  }
  * { margin: 0; padding: 0; box-sizing: border-box; }
  html, body {
    width: 1200px; height: 1200px; overflow: hidden;
    background: var(--page-bg);
  }
  .canvas {
    width: 1200px; height: 1200px;
    display: flex; align-items: center; justify-content: center;
  }
  .street-sign {
    position: relative;
    width: 1120px; height: 560px;
    background: var(--sign-white);
    overflow: hidden;
    box-shadow: 0 6px 18px rgba(40, 55, 90, 0.25);
    font-family: "Cinzel", serif;
  }
  .garden-backdrop {
    position: absolute; inset: 0;
    background:
      radial-gradient(ellipse 60% 22% at 50% 0%, var(--sage-glow) 0%, rgba(219,233,184,0) 100%),
      radial-gradient(ellipse 18% 12% at 92% 6%, #eef3c6 0%, rgba(238,243,198,0) 100%),
      radial-gradient(ellipse 70% 40% at 50% 60%, #ffffff 0%, rgba(255,255,255,0) 100%),
      linear-gradient(to bottom,
        #e4efc9 0%, #ffffff 22%, #ffffff 58%,
        #dfe8d2 72%, #b9c9a3 84%, var(--meadow-green) 93%, #c9b6a2 100%);
  }
  .garden-backdrop::after {
    content: ""; position: absolute; left: 0; right: 0; bottom: 0; height: 150px;
    background:
      radial-gradient(ellipse 12% 30% at 12% 70%, rgba(233,179,164,0.7), transparent),
      radial-gradient(ellipse 10% 28% at 38% 75%, rgba(240,190,170,0.6), transparent),
      radial-gradient(ellipse 12% 30% at 66% 72%, rgba(233,179,164,0.6), transparent),
      radial-gradient(ellipse 10% 28% at 90% 70%, rgba(230,160,160,0.6), transparent);
  }
  .sign-content {
    position: relative; z-index: 1;
    height: 100%;
    display: flex; flex-direction: column; align-items: center;
    padding-top: 56px;
  }
  .headline {
    color: var(--forest-green);
    font-weight: 800;
    font-size: 70px; line-height: 1;
    letter-spacing: 4px;
  }
  .headline-sub {
    color: var(--forest-green);
    font-weight: 800;
    font-size: 56px; line-height: 1;
    letter-spacing: 4px;
    margin-top: 10px;
  }
  .tagline {
    color: var(--clay-tan);
    font-weight: 700;
    font-size: 42px; line-height: 1;
    letter-spacing: 2px;
    margin-top: 30px;
  }
  .business-row {
    position: absolute; left: 30px; right: 30px; top: 385px;
    display: flex; justify-content: space-between; align-items: center;
  }
  .business-name {
    width: 340px;
    text-align: center;
    font-weight: 700;
    line-height: 1.05;
  }
  .business-name--growers { color: var(--forest-green); font-size: 34px; }
  .business-name--nook { color: var(--rose-pink); font-size: 44px; }
  .business-name--commons { color: var(--brick-maroon); font-size: 42px; }
  .business-name small { display: block; font-size: 19px; letter-spacing: 1px; margin-top: 6px; }
</style>
</head>
<body>
  <main class="canvas">
    <section class="street-sign" aria-label="Street sign for The Harlow Ridge Experience">
      <div class="garden-backdrop" role="img" aria-label="Soft-focus photograph of pastel roses and greenery along a wooden floor with sunlit bokeh above"></div>
      <div class="sign-content">
        <h1 class="headline">THE HARLOW RIDGE</h1>
        <h2 class="headline-sub">EXPERIENCE</h2>
        <p class="tagline">“Nature’s Best in One Place”</p>
        <div class="business-row">
          <p class="business-name business-name--growers">The Harlow Ridge<small>Growers &amp; Nursery</small></p>
          <p class="business-name business-name--nook">Bramble<br>Nook</p>
          <p class="business-name business-name--commons">Quarry<br>Commons</p>
        </div>
      </div>
    </section>
  </main>
</body>
</html>
```